Buchcover für ein Glücksbuch
Ich habe das erst Mal mir ein Buchcover erstellen lassen und bin sehr, sehr zufrieden. Gerne wieder!
Zielgruppe
Ich brauche ein Cover für mein Glücksbuch, es soll möglichst viele interessierte Leser ansprechen und zum Kauf des Buches animieren.
Mein Glücksbuch ist für jeden gedacht, der auch im Alltag in kleinen Dingen sein Glück sucht, es muss nicht immer das große Glück sein und auch Geld allein macht nicht glücklich. Es soll den Leser dazu bringen, das Glück in sich selbt zu finden. Es enthält Anleitungen und Tipps und eine Bonus-Mediation.
Aufgabenstellung
Der Titel des Buches lautet: 'Pfade zur Freude mit 12 Herzensmomenten'
Untertitel: 'Heiter und gelassen jeden Tag mit Ideen und Übungen zum Nachmachen'
'Mit Bonus-Meditation'
Autorin (Pseudonym): Maren Tosch

```html
<!DOCTYPE html>
<html lang="de">
<head>
<meta charset="utf-8">
<title>Pfade zur Freude – Buchcover</title>
<link rel="stylesheet" href="https://fonts.googleapis.com/css2?family=Amatic+SC:wght@400;700&family=Lexend:wght@500;600&display=swap">
<style>
  :root {
    --page: #ffffff;
    --leaf-dark: #0c220e;
    --leaf-mid: #1f5a22;
    --leaf-light: #4f9a3a;
    --leaf-sun: #6fb04a;
    --forest: #0d4a1c;
    --forest-glow: #1f9a40;
    --tendril: #c3e04a;
    --tendril-deep: #8cc43a;
    --accent-red: #d8262c;
    --band: #4aa63c;
    --band-glow: #d3ebca;
    --title-red: #e32f5c;
    --ink: #111111;
    --white: #ffffff;
  }
  * { box-sizing: border-box; margin: 0; padding: 0; }
  html, body {
    width: 900px; height: 1200px; overflow: hidden;
    background: var(--page);
  }
  .canvas { position: relative; width: 900px; height: 1200px; }

  .cover {
    position: absolute; left: 166px; top: 148px;
    width: 578px; height: 924px; overflow: hidden;
    box-shadow: 0 2px 10px rgba(0,0,0,0.18);
    font-family: "Lexend", sans-serif;
    color: var(--white);
  }

  .cover-photo-top {
    position: absolute; left: 0; top: 0; width: 100%; height: 113px;
    background:
      radial-gradient(ellipse 30% 60% at 20% 40%, rgba(79,154,58,0.8) 0%, rgba(79,154,58,0) 100%),
      radial-gradient(ellipse 35% 70% at 70% 85%, rgba(111,176,74,0.75) 0%, rgba(111,176,74,0) 100%),
      radial-gradient(ellipse 25% 55% at 90% 30%, rgba(79,154,58,0.6) 0%, rgba(79,154,58,0) 100%),
      linear-gradient(180deg, var(--leaf-dark) 0%, var(--leaf-mid) 100%);
  }
  .cover-photo-main {
    position: absolute; left: 0; top: 277px; width: 100%; height: 647px;
    background:
      radial-gradient(circle at 55% 68%, rgba(240,250,140,0.95) 0%, rgba(195,224,74,0.9) 7%, rgba(140,196,58,0.55) 18%, rgba(140,196,58,0) 34%),
      radial-gradient(ellipse 22% 30% at 33% 62%, rgba(195,224,74,0.45) 0%, rgba(195,224,74,0) 100%),
      radial-gradient(ellipse 28% 14% at 48% 86%, rgba(195,224,74,0.45) 0%, rgba(195,224,74,0) 100%),
      radial-gradient(ellipse 62% 34% at 44% 14%, rgba(111,176,74,0.95) 0%, rgba(79,154,58,0.7) 45%, rgba(79,154,58,0) 100%),
      radial-gradient(ellipse 30% 22% at 12% 8%, rgba(111,176,74,0.8) 0%, rgba(111,176,74,0) 100%),
      radial-gradient(ellipse at 85% 55%, var(--forest-glow) 0%, var(--forest) 55%, var(--leaf-dark) 100%);
  }

  .author {
    position: absolute; left: 0; right: 0; top: 34px;
    text-align: center; font-size: 24px; font-weight: 500;
  }

  .title-band {
    position: absolute; left: 0; top: 113px; width: 100%; height: 164px;
    background:
      radial-gradient(ellipse 48% 48% at 50% 50%, var(--band-glow) 0%, rgba(211,235,202,0.6) 55%, rgba(211,235,202,0) 100%),
      var(--band);
    text-align: center;
    font-family: "Amatic SC", cursive;
    font-weight: 700;
    text-transform: uppercase;
  }
  .title-main {
    position: absolute; left: 0; right: 0; top: 12px;
    font-size: 82px; line-height: 1; color: var(--title-red);
    letter-spacing: 1px;
  }
  .title-sub {
    position: absolute; left: 0; right: 0; top: 92px;
    font-size: 50px; line-height: 1; color: var(--ink);
    font-weight: 400; letter-spacing: 2px;
    -webkit-text-stroke: 0.6px var(--ink);
  }

  .subtitle {
    position: absolute; left: 0; top: 414px; width: 100%;
    font-size: 20px; font-weight: 600; line-height: 29px;
    text-shadow: 0 1px 3px rgba(0,0,0,0.35);
  }
  .subtitle span { display: block; white-space: nowrap; }
  .subtitle .l1 { padding-left: 250px; }
  .subtitle .l2 { padding-left: 262px; }
  .subtitle .l3 { padding-left: 318px; }
  .subtitle .l4 { padding-left: 292px; }

  .bonus {
    position: absolute; left: 380px; width: 140px; top: 810px;
    text-align: center; font-size: 18px; font-weight: 600; line-height: 23px;
    text-shadow: 0 1px 3px rgba(0,0,0,0.35);
  }
</style>
</head>
<body>
<div class="canvas">
  <div class="cover">
    <div class="cover-photo-top" role="img" aria-label="Foto: dunkelgrünes Blätterdach"></div>
    <div class="cover-photo-main" role="img" aria-label="Foto: großes Weinblatt über einer spiralförmigen hellgrünen Ranke mit zwei Marienkäfern vor grünem Hintergrund"></div>

    <div class="author">Maren Tosch</div>

    <div class="title-band">
      <h1 class="title-main">Pfade zur Freude</h1>
      <p class="title-sub">mit 12 Herzensmomenten</p>
    </div>

    <p class="subtitle">
      <span class="l1">Heiter und gelassen</span>
      <span class="l2">jeden Tag mit Ideen</span>
      <span class="l3">und Übungen</span>
      <span class="l4">zum Nachmachen</span>
    </p>

    <p class="bonus">Mit<br>Bonus-<br>Meditation</p>
  </div>
</div>
</body>
</html>
```